I want a website to be designed for our new company, it's an import and export company for variety of things.

please see the attached Logo for our company and the Images for our different sections for our busienss

Target Market(s)

multiple

Coding

Coded - Design and coding required

Number of Pages Required

5+ page

Font styles to use
Sans Serif

Colors

Designer to choose colors to be used in the design.

Requirements
Must have
• KOR GLOBAL
• KOR global Trading & Contracting provides various services. The Company offers infrastructure construction, oil, enegy and gas services, agricultural projects, real estate development, travel and tourism, and food processing and trading.
• Civil contracting for infrastructure, residential and heavy projects. Through its main subsidiaries; distribution of general food products, construction chemicals including corrosion inhibitors and electrical machinery; provides catering and travel agency services; ownership and operation of a school; offers human sources services including manpower supply.
• Drilling and Gold Mines Used Machinery, All Kinds of Construction Machinery, Drilling Machines are manufactured and sold.
Nice to have
• good designa and beautiful colours, it has too look professional

```html
<!DOCTYPE html>
<html lang="en">
<head>
<meta charset="utf-8">
<title>KOR GLOBAL – Trading &amp; Contracting</title>
<link href="https://fonts.googleapis.com/css2?family=Lato:wght@400;700;900&display=swap" rel="stylesheet">
<style>
:root{
  --gold:#b27d22;
  --green:#3b5620;
  --ink:#1d1d1d;
  --dark:#151515;
  --darker:#0f0f0f;
  --navy:#1e2c4c;
  --text:#555;
  --white:#fff;
}
*{margin:0;padding:0;box-sizing:border-box}
html,body{width:1200px;height:4518px;overflow:hidden}
body{position:relative;font-family:'Lato',sans-serif;color:var(--text);background:var(--white)}
.abs{position:absolute}
.btn{position:absolute;display:flex;align-items:center;justify-content:center;background:var(--green);color:var(--white);font-weight:900;font-size:15px;letter-spacing:.5px;height:43px}
.title{position:absolute;left:0;width:1200px;text-align:center;font-weight:900;font-size:28px;color:var(--ink);letter-spacing:.3px}
.title span,.h2 span{color:var(--gold)}
.h2{position:absolute;font-weight:900;font-size:28px;line-height:33px;color:var(--ink)}
.photo{position:absolute}
.p{font-size:13.5px;line-height:27px;color:var(--text)}

.topbar{left:0;top:0;width:1200px;height:50px;background:var(--ink)}
.topbar .phone{left:74px;top:14px;color:var(--white);font-size:15.5px;display:flex;align-items:center;gap:12px}
.social{display:flex;gap:20px}
.social i{display:block;width:20px;height:20px;border-radius:50%;background:var(--white)}
.nav{left:0;top:50px;width:1200px;height:96px;background:var(--dark)}
.nav a{position:absolute;top:43px;font-size:13.5px;font-weight:700;color:var(--white);text-decoration:none}
.nav a.active{color:var(--gold)}
.brandbox{left:490px;top:0;width:220px;height:146px;background:var(--darker);clip-path:polygon(0 0,100% 0,94% 100%,6% 100%)}
.brand{position:absolute;font-weight:700;color:var(--white);letter-spacing:3px;text-align:center;white-space:nowrap}

.hero{left:0;top:146px;width:1200px;height:576px;background:linear-gradient(180deg,#1f3f86 0%,#3b6bb0 35%,#b9b3a3 60%,#7a6447 78%,#5a4632 100%)}
.hero h1{position:absolute;left:0;top:232px;width:1200px;text-align:center;color:var(--white);font-size:50px;line-height:52px;font-weight:900}
.dots{left:560px;top:675px;display:flex;gap:15px}
.dots i{width:14px;height:14px;border-radius:50%;background:var(--white);display:block}
.dots i:first-child{background:var(--gold)}

.services{left:0;top:1178px;width:1200px;height:747px;background:radial-gradient(ellipse at 50% 45%,#fafafa 0%,#e9e9e9 70%,#e2e2e2 100%)}
.svc{position:absolute;width:335px}
.svc h3{font-size:17.5px;font-weight:900;color:var(--green);margin-bottom:6px;white-space:nowrap}
.svc p{font-size:13.5px;line-height:23px;width:292px}
.svc.l{text-align:right}
.svc.l p{margin-left:auto}
.ic{position:absolute;width:74px;height:74px;border-radius:50%;background:var(--white);box-shadow:0 2px 6px rgba(0,0,0,.15);display:flex;align-items:center;justify-content:center}
.ic.on{background:var(--gold)}

.card h4{position:absolute;width:331px;text-align:center;font-size:17.5px;font-weight:900;color:var(--green)}
.card p{position:absolute;width:331px;text-align:center;font-size:13.5px;line-height:23px}

.chair{left:0;top:2521px;width:1200px;height:479px;background:#e9e9e9}

.post .date{position:absolute;font-size:12px;font-weight:900;color:var(--gold)}
.post h5{position:absolute;font-size:17px;font-weight:900;color:var(--green)}
.post p{position:absolute;width:310px;font-size:13.5px;line-height:26px}

.reviews{left:0;top:3512px;width:1200px;height:523px;background:linear-gradient(180deg,#eaeaea,#fbfbfb 60%,#f2f2f2)}
.person{position:absolute;width:150px;text-align:center}
.person b{display:block;font-size:14px;font-weight:900;color:var(--ink)}
.person span{font-size:14px;color:var(--text)}
.avatar{position:absolute;width:100px;height:100px;border-radius:50%;background:linear-gradient(160deg,#d9d9d9,#8c8c8c)}

.news{left:0;top:4035px;width:1200px;height:88px;background:var(--green)}
.footer{left:0;top:4123px;width:1200px;height:332px;background:var(--ink)}
.footer h6{position:absolute;font-size:15px;font-weight:700;color:var(--white)}
.footer ul{position:absolute;list-style:none}
.footer li{font-size:13.5px;line-height:30.5px;color:var(--white)}
.contact{position:absolute;left:811px;font-size:13.5px;line-height:23px;color:#ddd}
.copy{left:0;top:4455px;width:1200px;height:63px;background:var(--darker);color:var(--white);font-size:13.5px;text-align:center;line-height:63px}
</style>
</head>
<body>

<div class="abs topbar">
  <div class="abs phone">
    <svg width="14" height="14" viewBox="0 0 24 24"><path fill="#b27d22" d="M6.6 10.8a15 15 0 006.6 6.6l2.2-2.2c.3-.3.7-.4 1-.2 1.1.4 2.3.6 3.6.6.6 0 1 .4 1 1V20c0 .6-.4 1-1 1A17 17 0 013 4c0-.6.4-1 1-1h3.5c.6 0 1 .4 1 1 0 1.3.2 2.5.6 3.6.1.3 0 .7-.2 1z"/></svg>
    +90 312 555 0140, &nbsp;+90 312 555 0141
  </div>
  <div class="abs social" style="right:74px;top:15px"><i></i><i></i><i></i><i></i><i></i></div>
</div>

<nav class="abs nav">
  <a class="active" style="left:109px">HOME</a>
  <a style="left:204px">ABOUT US</a>
  <a style="left:329px">OUR SERVICES</a>
  <a style="left:767px">PROJECTS</a>
  <a style="left:891px">BLOG</a>
  <a style="left:979px">CONTACT US</a>
</nav>
<div class="abs brandbox"></div>
<div class="brand" style="left:490px;top:60px;width:220px;font-size:20px">KOR GLOBAL</div>

<section class="abs hero" role="img" aria-label="Drilling rig spraying water on an arid hillside with a red drilling truck">
  <h1>DRILLING MACHINES<br>ARE MANUFACTURED AND SOLD</h1>
</section>
<div class="abs dots"><i></i><i></i><i></i></div>

<h2 class="h2" style="left:74px;top:786px">ABOUT <span>KOR GLOBAL TRADING</span><br><span>&amp; CONTRACTING COMPANY</span></h2>
<div class="abs p" style="left:74px;top:866px;width:600px">
  <p>KOR Global Trading &amp; Contracting provides various services. The Company offers infrastructure construction, oil, enegy and gas services, agricultural projects, real estate development, travel and tourism, and food processing and trading.</p>
  <p style="margin-top:9px">Civil contracting for infrastructure, residential and heavy projects. Through its main subsidiaries; distribution of general food products, construction chemicals including corrosion inhibitors and electrical machinery.</p>
</div>
<div class="btn" style="left:74px;top:1058px;width:180px">READ MORE</div>
<div class="abs" style="left:704px;top:788px;width:423px;height:310px;background:var(--navy)"></div>
<div class="photo" role="img" aria-label="Businessman in a dark suit holding a glowing world map" style="left:697px;top:796px;width:423px;height:309px;background:linear-gradient(135deg,#6f6f6f,#2a2a2a 55%,#4a4a4a)"></div>

<section class="abs services">
  <div class="title" style="top:62px">OUR <span>SERVICES</span></div>
  <svg class="abs" style="left:0;top:0" width="1200" height="747">
    <circle cx="601" cy="365" r="198" fill="none" stroke="#9a9a9a" stroke-width="1.2" stroke-dasharray="6 5"/>
    <circle cx="601" cy="365" r="152" fill="#141414"/>
  </svg>
  <div class="brand" style="left:449px;top:352px;width:304px;font-size:22px">KOR GLOBAL</div>

  <div class="ic" style="left:433px;top:167px"><svg width="34" height="34" viewBox="0 0 34 34"><path fill="#b27d22" d="M5 20a12 12 0 0124 0zM3 21h28v3H3z"/></svg></div>
  <div class="ic on" style="left:706px;top:167px"><svg width="34" height="34" viewBox="0 0 34 34"><path fill="#fff" d="M6 28C6 14 16 6 28 6c0 12-8 22-22 22z"/><path d="M6 28L20 14" stroke="#b27d22" stroke-width="2"/></svg></div>
  <div class="ic" style="left:365px;top:328px"><svg width="30" height="34" viewBox="0 0 30 34"><path fill="#b27d22" d="M15 2C15 2 4 16 4 22a11 11 0 0022 0C26 16 15 2 15 2z"/></svg></div>
  <div class="ic" style="left:768px;top:328px"><svg width="30" height="30" viewBox="0 0 24 24"><path fill="#b27d22" d="M21 16v-2l-8-5V3.5a1.5 1.5 0 00-3 0V9l-8 5v2l8-2.5V19l-2 1.5V22l3.5-1 3.5 1v-1.5L13 19v-5.5z"/></svg></div>
  <div class="ic" style="left:433px;top:482px"><svg width="32" height="32" viewBox="0 0 32 32"><circle cx="22" cy="9" r="5" fill="#b27d22"/><path fill="#b27d22" d="M2 28h28v3H2zM9 28V12h3v16z"/></svg></div>
  <div class="ic" style="left:706px;top:482px"><svg width="30" height="30" viewBox="0 0 24 24"><path fill="#b27d22" d="M12 3L2 12h3v8h5v-6h4v6h5v-8h3z"/></svg></div>

  <div class="svc l" style="left:70px;top:158px"><h3>INFRASTRUCTURE CONSTRUCTION</h3><p>Lorem ipsum dolor sit amet, consectetur adipiscing elit interdum massa sapien se fringilla sem blandit ac.</p></div>
  <div class="svc l" style="left:9px;top:323px"><h3>OIL</h3><p>Lorem ipsum dolor sit amet,<br>consectetur adipiscing elit interdu<br>mmassa sapien se fringilla</p></div>
  <div class="svc l" style="left:70px;top:479px"><h3>ENEGY AND GAS SERVICES</h3><p>Lorem ipsum dolor sit amet, consectetur adipiscing elit interdum massa sapien se fringilla sem blandit ac.</p></div>
  <div class="svc" style="left:797px;top:158px"><h3>AGRICULTURAL PROJECTS</h3><p>Lorem ipsum dolor sit amet, consectetur adipiscing elit interdum massa sapien se fringilla sem blandit ac.</p></div>
  <div class="svc" style="left:859px;top:306px;width:270px"><h3>TRAVEL AND TOURISM</h3><p style="width:260px">Lorem ipsum dolor sit amet, consectetur adipiscing elit interdum massa sapien se fringilla sem blandit ac.</p></div>
  <div class="svc" style="left:797px;top:479px"><h3>REAL ESTATE DEVELOPMENT</h3><p>Lorem ipsum dolor sit amet, consectetur adipiscing elit interdum massa sapien se fringilla sem blandit ac.</p></div>

  <div class="btn" style="left:488px;top:639px;width:226px">VIEW ALL SERVICES</div>
</section>

<div class="title" style="top:1993px">OUR <span>PROJECTS</span></div>
<div class="card">
  <div class="photo" role="img" aria-label="Yellow drilling machine in a snowy pine forest" style="left:74px;top:2060px;width:331px;height:213px;background:linear-gradient(180deg,#9fb4c2,#50626b 60%,#c9cfd3)"></div>
  <h4 style="left:74px;top:2298px">PROJECT HEADING</h4>
  <p style="left:74px;top:2325px">Lorem ipsum dolor sit amet, consectetur<br>adipiscing elit interdum.</p>
  <div class="btn" style="left:150px;top:2405px;width:180px">READ MORE</div>
</div>
<div class="card">
  <div class="photo" role="img" aria-label="Aerial view of a large building complex under construction" style="left:435px;top:2060px;width:331px;height:213px;background:linear-gradient(180deg,#8b8d85,#b5b3aa 50%,#6f7268)"></div>
  <h4 style="left:435px;top:2298px">PROJECT HEADING</h4>
  <p style="left:435px;top:2325px">Lorem ipsum dolor sit amet, consectetur<br>adipiscing elit interdum.</p>
  <div class="btn" style="left:511px;top:2405px;width:180px">READ MORE</div>
</div>
<div class="card">
  <div class="photo" role="img" aria-label="Offshore oil platform at sea" style="left:796px;top:2060px;width:331px;height:213px;background:linear-gradient(180deg,#c7b9a4,#4d6671 35%,#22394a)"></div>
  <h4 style="left:796px;top:2298px">PROJECT HEADING</h4>
  <p style="left:796px;top:2325px">Lorem ipsum dolor sit amet, consectetur<br>adipiscing elit interdum.</p>
  <div class="btn" style="left:872px;top:2405px;width:180px">READ MORE</div>
</div>

<section class="abs chair">
  <div class="abs" style="left:74px;top:82px;width:425px;height:310px;background:var(--navy)"></div>
  <div class="photo" role="img" aria-label="Portrait of the chairman in a navy suit in a bright office" style="left:81px;top:89px;width:425px;height:309px;background:linear-gradient(90deg,#c8cdd3,#8a95a5 40%,#e3e6ea)"></div>
  <h2 class="h2" style="left:533px;top:80px">CHAIRMAN <span>OF</span><br><span>THE BOARD MESSAGE</span></h2>
  <p class="abs p" style="left:533px;top:159px;width:580px">The underlying principle governing the operations of KOR Global Trading Company Limited is ‘Your Service Partner’, the common trait enabling us to consistently deliver our value promise to our customers, partners, employees and other stakeholders. As a privately owned and diversified service company, our strength is the result of an ever-widening range of activities conducted through a number of strategic business divisions.</p>
  <div class="btn" style="left:533px;top:349px;width:180px">READ MORE</div>
</section>

<div class="title" style="top:3063px">BLOG <span>POSTS</span></div>
<div class="post">
  <div class="photo" role="img" aria-label="Workers at an industrial construction site at sunset" style="left:74px;top:3132px;width:180px;height:130px;background:linear-gradient(135deg,#e0b57a,#7b6a5a)"></div>
  <div class="date" style="left:271px;top:3131px">JANUARY 18, 2019</div>
  <h5 style="left:271px;top:3151px">MAURIS ARCU TRISTIQUE URNA</h5>
  <p style="left:271px;top:3176px">Lorem ipsum dolor sit amet, consectetur adipiscing elit interdum a imperdiet ultrices, velit magna faucibus.</p>
</div>
<div class="post">
  <div class="photo" role="img" aria-label="Engineer with a tablet beside storage silos" style="left:614px;top:3132px;width:180px;height:130px;background:linear-gradient(135deg,#9aa4ad,#4f5457)"></div>
  <div class="date" style="left:811px;top:3131px">JANUARY 18, 2019</div>
  <h5 style="left:811px;top:3151px">MAURIS ARCU TRISTIQUE URNA</h5>
  <p style="left:811px;top:3176px">Lorem ipsum dolor sit amet, consectetur adipiscing elit interdum a imperdiet ultrices, velit magna faucibus.</p>
</div>
<div class="post">
  <div class="photo" role="img" aria-label="Offshore rig under a blue sky" style="left:74px;top:3309px;width:180px;height:129px;background:linear-gradient(180deg,#2f6fb5,#1f4d88)"></div>
  <div class="date" style="left:271px;top:3308px">JANUARY 18, 2019</div>
  <h5 style="left:271px;top:3328px">MAURIS ARCU TRISTIQUE URNA</h5>
  <p style="left:271px;top:3353px">Lorem ipsum dolor sit amet, consectetur adipiscing elit interdum a imperdiet ultrices, velit magna faucibus.</p>
</div>
<div class="post">
  <div class="photo" role="img" aria-label="Red drilling rig in a field under a blue sky" style="left:614px;top:3309px;width:180px;height:129px;background:linear-gradient(180deg,#3b7ccc,#86a6c6 60%,#8a5a44)"></div>
  <div class="date" style="left:811px;top:3308px">JANUARY 18, 2019</div>
  <h5 style="left:811px;top:3328px">MAURIS ARCU TRISTIQUE URNA</h5>
  <p style="left:811px;top:3353px">Lorem ipsum dolor sit amet, consectetur adipiscing elit interdum a imperdiet ultrices, velit magna faucibus.</p>
</div>

<section class="abs reviews">
  <div class="title" style="top:66px">CUSTOMER <span>REVIEWS</span></div>
  <svg class="abs" style="left:577px;top:142px" width="48" height="40" viewBox="0 0 48 40"><path fill="#3b5620" d="M0 0h20v20c0 10-6 18-16 20l-2-5c6-2 9-6 9-11H0zM26 0h20v20c0 10-6 18-16 20l-2-5c6-2 9-6 9-11H26z"/></svg>
  <p class="abs" style="left:160px;top:196px;width:880px;text-align:center;font-size:14px;line-height:27px">After days at sea, I really enjoy sitting in some coffeeshop, opening my computer and connecting with other Quillmora writers and work with words instead of ropes and sails. And more! With Quillmora, I have discovered some corners of the digital world that I would otherwise have never visited. So, even while working I keep traveling.</p>
  <svg class="abs" style="left:74px;top:262px" width="20" height="30"><path d="M17 2L4 15l13 13" fill="none" stroke="#333" stroke-width="3.5"/></svg>
  <svg class="abs" style="left:1106px;top:262px" width="20" height="30"><path d="M3 2l13 13L3 28" fill="none" stroke="#333" stroke-width="3.5"/></svg>
  <div class="avatar" role="img" aria-label="Customer portrait" style="left:393px;top:310px"></div>
  <div class="avatar" role="img" aria-label="Customer portrait" style="left:547px;top:310px;border:3px solid var(--gold)"></div>
  <div class="avatar" role="img" aria-label="Customer portrait" style="left:703px;top:310px"></div>
  <div class="person" style="left:368px;top:424px"><b>NAME HEADING</b><span>Location</span></div>
  <div class="person" style="left:522px;top:424px"><b>NAME HEADING</b><span>Location</span></div>
  <div class="person" style="left:678px;top:424px"><b>NAME HEADING</b><span>Location</span></div>
</section>

<section class="abs news">
  <div class="abs" style="left:74px;top:31px;color:#fff;font-size:20px;font-weight:900">NEWSLETTER SIGN UP</div>
  <div class="abs" style="left:321px;top:29px;width:302px;height:38px;background:#fff;font-size:12.5px;color:#555;padding:12px 12px">Enter Email Address</div>
  <div class="abs" style="left:630px;top:29px;width:111px;height:38px;background:var(--gold);color:#fff;font-size:12.5px;font-weight:700;text-align:center;line-height:38px">SIGN UP</div>
  <div class="abs social" style="right:74px;top:31px;gap:27px"><i style="width:24px;height:24px"></i><i style="width:24px;height:24px"></i><i style="width:24px;height:24px"></i><i style="width:24px;height:24px"></i><i style="width:24px;height:24px"></i></div>
</section>

<footer class="abs footer">
  <h6 style="left:79px;top:62px">SITE MAP</h6>
  <ul style="left:79px;top:85px"><li>Home</li><li>About Us</li><li>Services</li><li>Projects</li><li>Blog</li><li>Contact Us</li></ul>
  <h6 style="left:281px;top:62px">SERVICES</h6>
  <ul style="left:281px;top:85px"><li>Praesent consectetur</li><li>Dapibus lobortis</li><li>Fusce gravida nibh</li><li>Interdum</li><li>Pulvinar miin</li><li>Efficitur leo</li></ul>
  <div class="brand" style="left:500px;top:114px;width:200px;font-size:20px">KOR GLOBAL</div>
  <h6 style="left:811px;top:62px">CONTACT INFO</h6>
  <svg class="abs" style="left:811px;top:93px" width="10" height="14" viewBox="0 0 10 14"><path fill="#fff" d="M5 0a5 5 0 00-5 5c0 4 5 9 5 9s5-5 5-9a5 5 0 00-5-5zm0 7a2 2 0 110-4 2 2 0 010 4z"/></svg>
  <div class="contact" style="left:845px;top:88px">Meltem Sokak 14<br>No: 8/2 Cankaya / ANKARA / TURKEY</div>
  <svg class="abs" style="left:811px;top:160px" width="12" height="12" viewBox="0 0 24 24"><path fill="#fff" d="M6.6 10.8a15 15 0 006.6 6.6l2.2-2.2c.3-.3.7-.4 1-.2 1.1.4 2.3.6 3.6.6.6 0 1 .4 1 1V20c0 .6-.4 1-1 1A17 17 0 013 4c0-.6.4-1 1-1h3.5c.6 0 1 .4 1 1 0 1.3.2 2.5.6 3.6.1.3 0 .7-.2 1z"/></svg>
  <div class="contact" style="left:845px;top:153px">+90 312 555 0140 , &nbsp;+90 312 555 0141<br>+90 312 555 0142</div>
  <svg class="abs" style="left:811px;top:222px" width="13" height="10" viewBox="0 0 13 10"><path fill="#fff" d="M0 0h13v10H0z"/><path d="M0 0l6.5 5L13 0" fill="none" stroke="#1d1d1d" stroke-width="1.3"/></svg>
  <div class="contact" style="left:845px;top:215px">info@korglobal-example.com</div>
  <div class="contact" style="left:845px;top:250px">Map Location</div>
</footer>
<div class="abs copy">Copyright © 2020 CompanyName. All Right Reserved</div>

</body>
</html>
```